Hal's Remedies Business Card Design Project

I need a business card designed for my pharmacy Hal's Remedies. I would like just the logo on one side, maybe with black background and white lettering. The other side I would also like to include my logo which is attached. Also, please include my name and the following information:
Hal Norwick Owner/Pharm D.
Business address is 7163 N Birch Rd Sioux Falls, SD 57291.
Phone number is 605-318-6027 and fax # is 605-318-6031.
my email address is hal@halsremedies.example.
My website is www.halsremedies.example.
My business hours are Monday-Friday 8am-7 pm. Saturday 8am-12 pm. Sunday Closed.
I would like the design to include my logo colors, black, white, and neon green. Silver may be added as a highlight. Thanks.
Pharmacy
See above in product description

```html
<!DOCTYPE html>
<html lang="en">
<head>
<meta charset="utf-8">
<title>Hal's Remedies – Business Card</title>
<link rel="stylesheet" href="https://fonts.googleapis.com/css2?family=Open+Sans:wght@400;600&family=Questrial&display=swap">
<style>
  :root {
    --page-bg: #e2e2e2;
    --card-bg: #262728;
    --ink: #ffffff;
    --ink-soft: #e9e9e9;
    --neon: #a2cf30;
    --rule: #6a6a6a;
  }
  * { margin: 0; padding: 0; box-sizing: border-box; }
  html, body {
    width: 1000px; height: 1200px; overflow: hidden;
    background: var(--page-bg);
    font-family: "Open Sans", Arial, sans-serif;
  }
  .card {
    position: absolute; left: 168px;
    width: 655px; height: 393px;
    background: var(--card-bg);
    color: var(--ink);
  }
  .card--front { top: 117px; display: flex; align-items: center; justify-content: center; }
  .card--back { top: 675px; }

  .brand { display: flex; align-items: center; gap: 20px; }
  .brand__dot { width: 38px; height: 38px; border-radius: 50%; background: var(--neon); }
  .brand__name { font-weight: 600; font-size: 46px; letter-spacing: -1px; color: var(--ink); }
  .card--back .brand { position: absolute; left: 60px; top: 72px; gap: 14px; }
  .card--back .brand__dot { width: 24px; height: 24px; }
  .card--back .brand__name { font-size: 30px; letter-spacing: -0.6px; }

  .accent-bar { position: absolute; left: 0; top: 0; width: 13px; height: 100%; background: var(--neon); }
  .divider { position: absolute; left: 62px; top: 178px; width: 382px; height: 1px; background: var(--rule); }

  .owner { position: absolute; right: 58px; top: 165px; text-align: right; }
  .owner__name { font-family: "Questrial", Arial, sans-serif; font-size: 20px; letter-spacing: 1px; line-height: 24px; }
  .owner__title { font-family: "Questrial", Arial, sans-serif; font-size: 13px; color: var(--neon); letter-spacing: 0.5px; margin-top: 2px; }

  .contact { position: absolute; right: 58px; top: 236px; text-align: right; font-size: 12.5px; line-height: 15px; color: var(--ink-soft); letter-spacing: 0.2px; }
  .contact__group + .contact__group { margin-top: 9px; }
  .contact__label { color: var(--neon); }

  .hours { position: absolute; right: 411px; top: 302px; text-align: right; font-size: 12.5px; line-height: 15px; color: var(--ink-soft); letter-spacing: 0.2px; }
  .hours__closed { color: var(--neon); }
  .hours-rule { position: absolute; left: 253px; top: 299px; width: 1px; height: 48px; background: var(--rule); }
</style>
</head>
<body>
  <section class="card card--front" aria-label="Card front">
    <div class="brand">
      <span class="brand__dot"></span>
      <span class="brand__name">Hal's Remedies</span>
    </div>
  </section>

  <section class="card card--back" aria-label="Card back">
    <div class="accent-bar"></div>
    <div class="brand">
      <span class="brand__dot"></span>
      <span class="brand__name">Hal's Remedies</span>
    </div>
    <div class="divider"></div>
    <div class="owner">
      <p class="owner__name">Hal Norwick</p>
      <p class="owner__title">Owner/Pharm D.</p>
    </div>
    <div class="contact">
      <div class="contact__group">
        <p>7163 N Birch Rd</p>
        <p>Sioux Falls, SD 57291</p>
      </div>
      <div class="contact__group">
        <p><span class="contact__label">P.</span> 605-318-6027</p>
        <p><span class="contact__label">F</span> #605-318-6031</p>
      </div>
      <div class="contact__group">
        <p>hal@halsremedies.example</p>
        <p>www.halsremedies.example</p>
      </div>
    </div>
    <div class="hours">
      <p>Monday-Friday 8am-7 pm</p>
      <p>Saturday 8am-12 pm</p>
      <p class="hours__closed">Sunday Closed</p>
    </div>
    <div class="hours-rule"></div>
  </section>
</body>
</html>
```